Quorvallen

I need a webiste built to sell digital downloads. I will be selling audio books. I will be selling them by the book and also by the chapter. I already have logos (attached) and some examples of covers. I'd like it simple. I was thinking a banner with a "featured" product which scrolls between three of four and a list of products below. Clicking on one of the covers will then go to a purchase page, which will include an option to but the entire title or chapter. I want something similar to the marlo VISTA website in theme and design. In terms of tabs, I will need ABOUT, TRUE CRIME, SPORT, MUSIC, AUTHORS.

```html
<!DOCTYPE html>
<html lang="en">
<head>
<meta charset="utf-8">
<title>Quorvallen — Audiobooks</title>
<link href="https://fonts.googleapis.com/css2?family=Inter:wght@400;500;600;700&family=Permanent+Marker&display=swap" rel="stylesheet">
<style>
:root{
  --green:#6ab42d;
  --green-dark:#4f8f1c;
  --green-soft:#dcf3c6;
  --ink:#1d1d1f;
  --muted:#555;
  --dark:#1c1d21;
  --hero:#2a2b30;
  --pale:#f0f1f5;
  --white:#fff;
  --star:#f2b01e;
  --display:'Permanent Marker',cursive;
  --body:'Inter',Arial,sans-serif;
}
*{box-sizing:border-box;margin:0;padding:0}
html,body{width:1200px;height:3883px;overflow:hidden}
body{position:relative;font-family:var(--body);color:var(--ink);background:var(--white)}
.abs{position:absolute}

/* nav */
.site-nav{left:0;top:0;width:1200px;height:62px;background:var(--white);box-shadow:0 1px 4px rgba(0,0,0,.08);z-index:2}
.brand{left:100px;top:13px;font-weight:700;font-size:26px;color:var(--green);display:flex;align-items:center;gap:8px}
.brand .dot{width:14px;height:14px;border-radius:50%;background:var(--green)}
.nav-links{left:424px;top:23px;display:flex;gap:33px;font-size:15px;list-style:none}
.nav-links li{color:#333}
.nav-links .active{color:var(--green);border-bottom:2px solid var(--green);padding-bottom:4px}

/* hero */
.hero{left:0;top:62px;width:1200px;height:523px;background:linear-gradient(135deg,#2e2f35,#1e1f23 60%,#2a2b31)}
.hero-art{left:0;top:0;width:648px;height:523px;background:linear-gradient(100deg,#9a9a9a 0%,#5d5d60 40%,#1a1a1c 60%,#2a1416 75%,#3a0f12 100%)}
.hero-copy{left:704px;top:145px;width:380px;color:#eee}
.hero-title{font-weight:700;font-size:48px;color:var(--white);letter-spacing:1px}
.hero-copy p{font-size:12.5px;line-height:21px;margin-top:10px}
.search{left:704px;top:274px;width:374px;height:47px;background:var(--white);border-radius:24px;padding:0 22px;display:flex;align-items:center;justify-content:space-between;font-size:14px;color:#777}

/* carousels */
.band-pale{left:0;width:1200px;background:var(--pale)}
.section-title{font-family:var(--display);color:var(--green);font-size:50px;line-height:46px;text-shadow:2px 2px 0 #1d3d09}
.rail-label{font-size:12px;color:#333;display:flex;align-items:center;gap:12px}
.rail-label::after{content:"";width:108px;height:1px;background:#bbb}
.arrows{display:flex;gap:10px}
.arrow{width:80px;height:42px;background:var(--white);border-radius:4px;box-shadow:0 2px 6px rgba(0,0,0,.08);display:flex;align-items:center;justify-content:center}
.card{width:214px;height:285px;background:var(--white);box-shadow:0 2px 8px rgba(0,0,0,.12)}
.card .clip{position:absolute;left:8px;top:9px;font-size:11px;color:var(--green);border:1px solid var(--green);border-radius:10px;padding:1px 8px;z-index:1}
.card .cover{position:absolute;left:60px;top:8px;width:120px;height:150px;border-radius:50% 50% 8px 8px;background:radial-gradient(circle at 50% 60%,#2f8a4c 0,#2c7a43 40%,#7fdcd6 62%,#fff 66%)}
.card h3{position:absolute;left:12px;top:178px;font-size:15.5px;font-weight:500;white-space:nowrap}
.card .by{position:absolute;left:12px;top:198px;font-size:11px}
.card .pub{position:absolute;left:12px;top:215px;font-size:10px;color:var(--muted)}
.card .stars{position:absolute;left:12px;top:229px;font-size:11px;color:var(--star);letter-spacing:1px}
.card .kind{position:absolute;left:0;bottom:0;width:100%;height:36px;background:var(--green-soft);color:var(--green);font-size:14px;display:flex;align-items:center;justify-content:center}

/* authors */
.author{width:233px;height:235px;background:var(--white);box-shadow:0 2px 8px rgba(0,0,0,.12)}
.author .photo{position:absolute;left:7px;top:7px;width:219px;height:173px}
.author .name{position:absolute;left:12px;top:192px;font-size:13.5px}
.author .see{position:absolute;right:10px;top:210px;font-size:13px;color:var(--green)}

/* testimonials */
.quote{width:455px;height:218px;background:var(--white);box-shadow:0 2px 10px rgba(0,0,0,.12);padding:20px 20px}
.quote .mark{width:50px;height:50px;border-radius:50%;background:var(--green);color:var(--white);font-size:40px;font-weight:700;display:flex;align-items:center;justify-content:center;padding-top:14px}
.quote h4{font-size:16px;font-weight:500;margin-top:14px}
.quote small{font-size:8px;display:block}
.quote p{font-size:12.5px;line-height:27px;color:#333;text-align:justify;margin-top:6px}

/* blog */
.post{width:318px}
.post .thumb{height:202px}
.post .date{font-size:12px;color:var(--green);margin:18px 0 0 8px}
.post h3{font-size:17.5px;font-weight:600;line-height:23px;margin:8px 0 0 8px}
.post p{font-size:12px;line-height:23px;color:#444;margin:10px 0 0 8px}
.btn{display:inline-block;margin:12px 0 0 8px;background:var(--green);color:var(--white);font-weight:600;font-size:15px;padding:10px 27px;border-radius:22px}

/* footer */
.footer{left:0;top:3500px;width:1200px;height:383px;background:var(--dark);color:#eee}
.foot-brand{left:100px;top:175px;font-size:30px;font-weight:700;color:var(--green);display:flex;gap:10px;align-items:center}
.foot-brand .dot{width:18px;height:18px;border-radius:50%;background:var(--green)}
.foot-col h5{font-size:15px;font-weight:700;margin-bottom:12px}
.foot-col ul{list-style:none;font-size:14px;line-height:31px}
.social{left:918px;top:263px;display:flex;gap:8px}
.social span{width:38px;height:38px;border:1.5px solid #eee;border-radius:50%;font-size:9px;display:flex;align-items:center;justify-content:center}
.foot-rule{left:100px;top:327px;width:1000px;height:1px;background:#444}
.copy{left:0;top:348px;width:1200px;text-align:center;font-size:13px}
</style>
</head>
<body>

<header class="abs site-nav">
  <div class="abs brand"><span class="dot"></span>Quorvallen</div>
  <ul class="abs nav-links">
    <li class="active">HOME</li><li>ABOUT</li><li>TRUE CRIME</li><li>SPORT</li><li>MUSIC</li><li>AUTHORS</li><li>CONTACT US</li>
  </ul>
</header>

<section class="abs hero">
  <div class="abs hero-art" role="img" aria-label="Featured true crime audiobook cover artwork with portrait and hand-lettered title"></div>
  <div class="abs hero-copy">
    <div class="hero-title">Quorvallen</div>
    <p>Lorem ipsum dolor sit amet, consectetur adipiscing elit, sed do eiusmod tempor incididunt</p>
  </div>
  <div class="abs search">Search Audiobooks ...
    <svg width="22" height="22" viewBox="0 0 22 22" fill="none" stroke="#6ab42d" stroke-width="1.8"><circle cx="10" cy="10" r="7.5"/><path d="M15.5 15.5L20 20"/></svg>
  </div>
</section>

<!-- rails -->
<section class="abs band-pale" style="top:585px;height:382px"></section>

<svg width="0" height="0" style="position:absolute"><defs>
<symbol id="arr-l" viewBox="0 0 36 14"><path d="M35 7H2M8 1L2 7l6 6" fill="none" stroke="#222" stroke-width="1.6"/></symbol>
<symbol id="arr-r" viewBox="0 0 36 14"><path d="M1 7h33M28 1l6 6-6 6" fill="none" stroke="#222" stroke-width="1.6"/></symbol>
</defs></svg>

<div class="abs section-title" style="left:100px;top:668px">MOST<br>POPULAR</div>
<div class="abs rail-label" style="left:100px;top:784px">Free audiobooks</div>
<div class="abs arrows" style="left:100px;top:818px"><div class="arrow"><svg width="36" height="14"><use href="#arr-l"/></svg></div><div class="arrow"><svg width="36" height="14"><use href="#arr-r"/></svg></div></div>

<div class="abs section-title" style="left:100px;top:1096px">TRUE<br>CRIME</div>
<div class="abs rail-label" style="left:100px;top:1213px">Audiobooks</div>
<div class="abs arrows" style="left:100px;top:1248px"><div class="arrow"><svg width="36" height="14"><use href="#arr-l"/></svg></div><div class="arrow"><svg width="36" height="14"><use href="#arr-r"/></svg></div></div>

<div class="abs section-title" style="left:100px;top:1452px">SPORT<br>ON</div>
<div class="abs rail-label" style="left:100px;top:1569px">Audiobooks</div>
<div class="abs arrows" style="left:100px;top:1603px"><div class="arrow"><svg width="36" height="14"><use href="#arr-l"/></svg></div><div class="arrow"><svg width="36" height="14"><use href="#arr-r"/></svg></div></div>

<!-- row 1 -->
<article class="abs card" style="left:345px;top:622px"><span class="clip">▶ Clip</span><div class="cover" role="img" aria-label="Audiobook cover: book with headphones"></div><h3>The standard Lorem</h3><div class="by">By John Smith</div><div class="pub">Finibus Bonorum</div><div class="stars">★★★★★</div><div class="kind">Audiobook</div></article>
<article class="abs card" style="left:585px;top:622px"><span class="clip">▶ Clip</span><div class="cover" role="img" aria-label="Audiobook cover: book with headphones"></div><h3>The standard Lorem</h3><div class="by">By John Smith</div><div class="pub">Finibus Bonorum</div><div class="stars">★★★★★</div><div class="kind">Audiobook</div></article>
<article class="abs card" style="left:826px;top:622px"><span class="clip">▶ Clip</span><div class="cover" role="img" aria-label="Audiobook cover: book with headphones"></div><h3>The standard Lorem</h3><div class="by">By John Smith</div><div class="pub">Finibus Bonorum</div><div class="stars">★★★★★</div><div class="kind">Audiobook</div></article>
<article class="abs card" style="left:1066px;top:622px"><span class="clip">▶ Clip</span><div class="cover" role="img" aria-label="Audiobook cover: book with headphones"></div><h3>The standard Lorem</h3><div class="by">By John Smith</div><div class="pub">Finibus Bonorum</div><div class="stars">★★★★★</div><div class="kind">Audiobook</div></article>
<!-- row 2 -->
<article class="abs card" style="left:345px;top:1050px"><span class="clip">▶ Clip</span><div class="cover" role="img" aria-label="Audiobook cover: book with headphones"></div><h3>The standard Lorem</h3><div class="by">By John Smith</div><div class="pub">Finibus Bonorum</div><div class="stars">★★★★★</div><div class="kind">Audiobook</div></article>
<article class="abs card" style="left:585px;top:1050px"><span class="clip">▶ Clip</span><div class="cover" role="img" aria-label="Audiobook cover: book with headphones"></div><h3>The standard Lorem</h3><div class="by">By John Smith</div><div class="pub">Finibus Bonorum</div><div class="stars">★★★★★</div><div class="kind">Audiobook</div></article>
<article class="abs card" style="left:826px;top:1050px"><span class="clip">▶ Clip</span><div class="cover" role="img" aria-label="Audiobook cover: book with headphones"></div><h3>The standard Lorem</h3><div class="by">By John Smith</div><div class="pub">Finibus Bonorum</div><div class="stars">★★★★★</div><div class="kind">Audiobook</div></article>
<article class="abs card" style="left:1066px;top:1050px"><span class="clip">▶ Clip</span><div class="cover" role="img" aria-label="Audiobook cover: book with headphones"></div><h3>The standard Lorem</h3><div class="by">By John Smith</div><div class="pub">Finibus Bonorum</div><div class="stars">★★★★★</div><div class="kind">Audiobook</div></article>
<!-- row 3 -->
<article class="abs card" style="left:345px;top:1406px"><span class="clip">▶ Clip</span><div class="cover" role="img" aria-label="Audiobook cover: book with headphones"></div><h3>The standard Lorem</h3><div class="by">By John Smith</div><div class="pub">Finibus Bonorum</div><div class="stars">★★★★★</div><div class="kind">Audiobook</div></article>
<article class="abs card" style="left:585px;top:1406px"><span class="clip">▶ Clip</span><div class="cover" role="img" aria-label="Audiobook cover: book with headphones"></div><h3>The standard Lorem</h3><div class="by">By John Smith</div><div class="pub">Finibus Bonorum</div><div class="stars">★★★★★</div><div class="kind">Audiobook</div></article>
<article class="abs card" style="left:826px;top:1406px"><span class="clip">▶ Clip</span><div class="cover" role="img" aria-label="Audiobook cover: book with headphones"></div><h3>The standard Lorem</h3><div class="by">By John Smith</div><div class="pub">Finibus Bonorum</div><div class="stars">★★★★★</div><div class="kind">Audiobook</div></article>
<article class="abs card" style="left:1066px;top:1406px"><span class="clip">▶ Clip</span><div class="cover" role="img" aria-label="Audiobook cover: book with headphones"></div><h3>The standard Lorem</h3><div class="by">By John Smith</div><div class="pub">Finibus Bonorum</div><div class="stars">★★★★★</div><div class="kind">Audiobook</div></article>

<!-- authors -->
<section class="abs band-pale" style="top:1773px;height:679px"></section>
<h2 class="abs section-title" style="left:0;width:1200px;text-align:center;top:1830px;font-weight:400">FIND AUTHORS</h2>

<div class="abs author" style="left:100px;top:1900px"><div class="photo" role="img" aria-label="Author portrait photo" style="background:linear-gradient(#cfcfcf,#a9a59c)"></div><div class="name">John Smith</div><div class="see">See All</div></div>
<div class="abs author" style="left:355px;top:1900px"><div class="photo" role="img" aria-label="Author portrait photo" style="background:linear-gradient(#d9d9d9,#6f98b8)"></div><div class="name">John Smith</div><div class="see">See All</div></div>
<div class="abs author" style="left:611px;top:1900px"><div class="photo" role="img" aria-label="Author writing at a desk" style="background:linear-gradient(#4a4a48,#8a7d6a)"></div><div class="name">John Smith</div><div class="see">See All</div></div>
<div class="abs author" style="left:866px;top:1900px"><div class="photo" role="img" aria-label="Author working at a desk with headphones" style="background:linear-gradient(#3e4036,#5f6b4a)"></div><div class="name">John Smith</div><div class="see">See All</div></div>
<div class="abs author" style="left:100px;top:2158px"><div class="photo" role="img" aria-label="Author portrait photo" style="background:linear-gradient(#dedede,#d0ccc6)"></div><div class="name">John Smith</div><div class="see">See All</div></div>
<div class="abs author" style="left:355px;top:2158px"><div class="photo" role="img" aria-label="Author portrait photo" style="background:linear-gradient(#3b79b5,#5c8fc2)"></div><div class="name">John Smith</div><div class="see">See All</div></div>
<div class="abs author" style="left:611px;top:2158px"><div class="photo" role="img" aria-label="Author portrait photo" style="background:linear-gradient(#cfc9bf,#1f5a4a)"></div><div class="name">John Smith</div><div class="see">See All</div></div>
<div class="abs author" style="left:866px;top:2158px"><div class="photo" role="img" aria-label="Author portrait photo" style="background:linear-gradient(#e3e3e3,#45577a)"></div><div class="name">John Smith</div><div class="see">See All</div></div>

<!-- testimonials -->
<h2 class="abs section-title" style="left:0;width:1200px;text-align:center;top:2516px;font-weight:400">WHAT PEOPLE ARE SAYING...</h2>
<div class="abs quote" style="left:127px;top:2600px"><div class="mark">“</div><h4>John Smith</h4><small>Finibus Bonorum</small><p>Lorem ipsum dolor sit ectetur ipiscing elit, sed do or incididunt ut labore et dolorealiqua. Quis ipsum spendisse ultrices graviodo viverra maecenas accumsan lacus vel facilisis.</p></div>
<div class="abs quote" style="left:617px;top:2600px"><div class="mark">“</div><h4>John Smith</h4><small>Finibus Bonorum</small><p>Lorem ipsum dolor sit ectetur ipiscing elit, sed do or incididunt ut labore et dolorealiqua. Quis ipsum spendisse ultrices graviodo viverra maecenas accumsan lacus vel facilisis.</p></div>

<!-- blog -->
<section class="abs band-pale" style="top:2893px;height:607px"></section>
<h2 class="abs section-title" style="left:0;width:1200px;text-align:center;top:2954px;font-weight:400">RECENT BLOGPOSTS</h2>
<article class="abs post" style="left:97px;top:3030px"><div class="thumb" role="img" aria-label="Person working on a laptop in a dim room" style="background:linear-gradient(135deg,#2a1d14,#8a5a34 50%,#3b2618)"></div><div class="date">▣ SPE 8, 2023</div><h3>The standard Lorem Ipsum passage, used since the 1500s</h3><p>Lorem ipsum dolor sit amet, consectetur adipiscing elit, sed do eiusmod tempor incididunt ut labore et dolore magna aliqua.</p><span class="btn">LEARN MORE</span></article>
<article class="abs post" style="left:438px;top:3030px"><div class="thumb" role="img" aria-label="Headphones resting on an open book" style="background:radial-gradient(circle at 50% 40%,#e8d6f2,#8a4fa3 45%,#2a1436)"></div><div class="date">▣ SPE 8, 2023</div><h3>The standard Lorem Ipsum passage, used since the 1500s</h3><p>Lorem ipsum dolor sit amet, consectetur adipiscing elit, sed do eiusmod tempor incididunt ut labore et dolore magna aliqua.</p><span class="btn">LEARN MORE</span></article>
<article class="abs post" style="left:779px;top:3030px"><div class="thumb" role="img" aria-label="Headphones on a stack of books" style="background:linear-gradient(135deg,#d8cdb8,#c9a22a 45%,#2b2b2b)"></div><div class="date">▣ SPE 8, 2023</div><h3>The standard Lorem Ipsum passage, used since the 1500s</h3><p>Lorem ipsum dolor sit amet, consectetur adipiscing elit, sed do eiusmod tempor incididunt ut labore et dolore magna aliqua.</p><span class="btn">LEARN MORE</span></article>

<!-- footer -->
<footer class="abs footer">
  <div class="abs foot-brand"><span class="dot"></span>Quorvallen</div>
  <div class="abs foot-col" style="left:466px;top:126px"><h5>Links</h5><ul><li>Home</li><li>About</li><li>True Crime</li><li>Sport</li></ul></div>
  <div class="abs foot-col" style="left:592px;top:156px"><ul><li>Music</li><li>Authors</li><li>Contact Us</li></ul></div>
  <div class="abs foot-col" style="left:793px;top:126px"><h5>COMPANY</h5><ul><li>About</li><li>Blog</li><li>Press</li></ul></div>
  <div class="abs foot-col" style="left:1005px;top:126px"><h5>LEGAL</h5><ul><li>Privacy</li><li>Terms</li><li>Cookie policy</li></ul></div>
  <div class="abs social"><span>Echo</span><span>Wave</span><span>Kite</span><span>Loop</span></div>
  <div class="abs foot-rule"></div>
  <div class="abs copy">©Copyright 2023 Quorvallen. All Rights Reserved.</div>
</footer>

</body>
</html>
```